Graphical design for food product in 1 Liter carton

We need this design not for a real product but as a showcase for a new service.

This special situation makes it really simple for you to participate because you only have to care about how the visual impression of your design is.

Furthermore it gives you the opportunity to get an extra winning chance if you choose to also participate in the open competition at our website - where you can enter the same design as you enter here at ArtQuarry.

Here is the requirements:

1. You must apply your design to our attatched template

2. Make a design for a food product of your own choice, which is to be sold from retail stores in a rectangular 1 L carton – based on our template.

3. You are only allowed to use brand names and/or logos that you have the rights to use for this competition, so please make completely fictive brand names and logos.

4. Your design is evaluated on the visual impression only, which means that your text on the design can be in any language and doesn’t have to relate to the design.

5. The criteria for the evaluation of your design is your creativity, the graphical quality and how well the product will display it self in the stores.

If you also want to participate in the open competition on our website - where you can win an Zelbo Slate, and will get your design skills exposed to brand owners and packaging manufacturers all over the world, then please visit plovimark.example/packaging-design-competition/

Attatched is:

A. Empty design template you must apply your design to. Remove the layer with our template when you return your send in your design.

B. Example of design applied to the template.

C. Example of the applied example design after it has been converted to 3D with our online 3D engine at PloviMark.example.

The winning design will be converted to 3D and will be used as a showcase on our website - all designers can enter their design to our open competition at PloviMark.example.

```html
<!DOCTYPE html>
<html lang="en">
<head>
<meta charset="utf-8">
<title>Cherry Juice – 1 L Carton Dieline</title>
<link rel="stylesheet" href="https://fonts.googleapis.com/css2?family=Marcellus&family=Great+Vibes&family=Alegreya+Sans:wght@400;700&display=swap">
<style>
  :root {
    --paper: #ffffff;
    --ink-black: #000000;
    --deep-green: #0a1f05;
    --mid-green: #2f6a12;
    --leaf-green: #4f8f1c;
    --glow-green: #c9e25a;
    --gold: #e8c25a;
    --gold-dark: #a27a1e;
    --cream: #fbf3d6;
    --cherry-red: #b5121b;
    --rust: #a2380a;
    --rust-light: #d7883a;
    --body-text: #f4f4ec;
  }
  html, body {
    margin: 0;
    padding: 0;
    overflow: hidden;
    background: var(--paper);
  }
  .carton-canvas {
    width: 1188px;
    height: 1200px;
    display: block;
  }
  .brand-word { font-family: "Marcellus", serif; fill: var(--rust-light); }
  .flavour-caps { font-family: "Marcellus", serif; fill: var(--gold); letter-spacing: 0.5px; }
  .script-word { font-family: "Great Vibes", cursive; fill: var(--cream); }
  .ribbon-word { font-family: "Great Vibes", cursive; fill: var(--cream); }
  .body-copy { font-family: "Alegreya Sans", sans-serif; fill: var(--body-text); font-size: 8.3px; }
</style>
</head>
<body>
<svg class="carton-canvas" viewBox="0 0 1031 1041" preserveAspectRatio="none" xmlns="http://www.w3.org/2000/svg">
  <defs>
    <linearGradient id="flap-green" x1="0" y1="0" x2="0" y2="1">
      <stop offset="0" stop-color="var(--leaf-green)"/>
      <stop offset="1" stop-color="var(--deep-green)"/>
    </linearGradient>
    <linearGradient id="roof-green" x1="0" y1="0" x2="0" y2="1">
      <stop offset="0" stop-color="#050a02"/>
      <stop offset="1" stop-color="#173a08"/>
    </linearGradient>
    <radialGradient id="panel-glow" cx="0.5" cy="0.5" r="0.6">
      <stop offset="0" stop-color="var(--glow-green)"/>
      <stop offset="0.35" stop-color="var(--leaf-green)"/>
      <stop offset="0.75" stop-color="#173d08"/>
      <stop offset="1" stop-color="#030801"/>
    </radialGradient>
    <radialGradient id="arch-glow" cx="0.5" cy="0.3" r="0.7">
      <stop offset="0" stop-color="#d6ea7a"/>
      <stop offset="0.5" stop-color="#7fb235"/>
      <stop offset="1" stop-color="#2f6a12" stop-opacity="0"/>
    </radialGradient>
    <linearGradient id="rust-band" x1="0" y1="0" x2="0" y2="1">
      <stop offset="0" stop-color="var(--rust-light)"/>
      <stop offset="0.4" stop-color="var(--rust)"/>
      <stop offset="1" stop-color="#8a2a04"/>
    </linearGradient>
    <linearGradient id="ribbon-green" x1="0" y1="0" x2="0" y2="1">
      <stop offset="0" stop-color="#4f8a26"/>
      <stop offset="1" stop-color="#1d4a0b"/>
    </linearGradient>

    <!-- top flap with wordmark -->
    <g id="top-flap">
      <rect x="0" y="0" width="256" height="212" fill="url(#flap-green)"/>
      <rect x="18" y="10" width="232" height="190" fill="none" stroke="var(--gold)" stroke-width="1.5"/>
      <text class="flavour-caps" x="35" y="158" font-size="27">CHERRY</text>
      <circle cx="191" cy="146" r="14" fill="var(--cherry-red)" role="img" aria-label="Cherry illustration"/>
      <text class="script-word" x="108" y="182" font-size="34">Juice</text>
    </g>

    <!-- roof flap with ribbon -->
    <g id="roof-flap">
      <polygon points="0,212 128,68 256,212" fill="url(#roof-green)"/>
      <path d="M68,150 L178,136 L186,180 L74,194 Z" fill="url(#ribbon-green)" stroke="#9fd05a" stroke-width="0.8"/>
      <text class="ribbon-word" x="88" y="178" font-size="22" transform="rotate(-7 128 170)">Organic</text>
    </g>

    <!-- front panel -->
    <g id="front-panel">
      <rect x="0" y="212" width="257" height="700" fill="url(#panel-glow)"/>
      <rect x="24" y="238" width="208" height="674" fill="none" stroke="var(--gold)" stroke-width="1.3"/>
      <path d="M32,830 L32,500 Q32,430 127,430 Q222,430 222,500 L222,830 Z" fill="url(#arch-glow)"/>
      <text class="brand-word" x="128" y="298" font-size="25" text-anchor="middle">Evergrove</text>
      <text class="brand-word" x="128" y="330" font-size="12" text-anchor="middle" letter-spacing="2">Country Foods</text>
      <path d="M62,392 L202,378 L208,424 L68,440 Z" fill="url(#ribbon-green)" stroke="#9fd05a" stroke-width="0.8"/>
      <text class="ribbon-word" x="88" y="426" font-size="27" transform="rotate(-6 135 412)">Organic</text>
      <rect x="34" y="480" width="196" height="192" rx="14" fill="#8a1a22" opacity="0.85" role="img" aria-label="Illustration of a glass of cherry juice with cherries, blossom and leaves"/>
      <rect x="40" y="680" width="196" height="56" rx="26" fill="#1f5010" stroke="var(--gold)" stroke-width="2"/>
      <text class="flavour-caps" x="131" y="718" font-size="27" text-anchor="middle">CHERRY</text>
      <text class="script-word" x="126" y="808" font-size="60" text-anchor="middle">Juice</text>
      <rect x="26" y="838" width="200" height="59" fill="url(#rust-band)"/>
    </g>

    <!-- back panel -->
    <g id="back-panel">
      <rect x="0" y="212" width="256" height="700" fill="url(#panel-glow)"/>
      <rect x="26" y="238" width="204" height="674" fill="none" stroke="var(--leaf-green)" stroke-width="1.3"/>
      <text class="body-copy">
        <tspan x="56" y="310">Lorem ipsum dolor sit amet,</tspan>
        <tspan x="56" y="321">consectetuer adipiscing elit. Praesent a</tspan>
        <tspan x="56" y="332">lacus vitae turpis consequat semper.</tspan>
        <tspan x="56" y="343">Pellentesque condimentum felis a sem.</tspan>
        <tspan x="56" y="354">Vivamus feugiat. Aenean justo ipsum,</tspan>
        <tspan x="56" y="365">luctus ut, volutpat laoreet, vehicula in,</tspan>
        <tspan x="56" y="376">libero. In tempus urna. Vivamus quis</tspan>
        <tspan x="56" y="387">mi.</tspan>
        <tspan x="56" y="418">Lorem ipsum dolor sit amet,</tspan>
        <tspan x="56" y="429">consectetuer adipiscing elit.</tspan>
        <tspan x="56" y="455">Aliquam sed erat. Quisque vehicula</tspan>
        <tspan x="56" y="466">porttitor odio. Proin dolor sapien,</tspan>
        <tspan x="56" y="477">adipiscing id, sagittis eu, molestie</tspan>
        <tspan x="56" y="488">viverra, mauris. Curabitur nunc ante,</tspan>
        <tspan x="56" y="499">ullamcorper vel, auctor a, aliquam at,</tspan>
        <tspan x="56" y="510">tortor.</tspan>
        <tspan x="56" y="540">Vivamus nisi elit, nonummy id, facilisis</tspan>
        <tspan x="56" y="551">non, blandit ac, dolor. Mauris urna</tspan>
        <tspan x="56" y="562">sem, suscipit vitae, dignissim id, ultrices</tspan>
        <tspan x="56" y="573">sed, nunc. Nam nisl quam, posuere</tspan>
      </text>
      <text class="flavour-caps" x="56" y="642" font-size="24">CHERRY</text>
      <text class="script-word" x="118" y="668" font-size="32">Juice</text>
      <rect x="68" y="680" width="100" height="90" rx="30" fill="var(--cherry-red)" opacity="0.85" role="img" aria-label="Illustration of cherries with blossom and leaves"/>
      <text class="brand-word" x="128" y="803" font-size="16" text-anchor="middle">Evergrove</text>
      <text class="brand-word" x="128" y="822" font-size="8.5" text-anchor="middle" letter-spacing="1.5">Country Foods</text>
    </g>
  </defs>

  <rect x="0" y="0" width="1031" height="1041" fill="var(--paper)"/>
  <rect x="0" y="212" width="1031" height="829" fill="var(--ink-black)"/>

  <use href="#top-flap" x="0" y="0"/>
  <use href="#roof-flap" x="258" y="0"/>
  <use href="#top-flap" x="516" y="0"/>
  <use href="#roof-flap" x="772" y="-3"/>

  <use href="#front-panel" x="0" y="0"/>
  <use href="#back-panel" x="258" y="0"/>
  <use href="#front-panel" x="516" y="0"/>
  <use href="#back-panel" x="772" y="0"/>
</svg>
</body>
</html>
```